Flyer for Brand New Montessori School

Quiet Harbor Academy is opening in the fall to students infant-5th grade. We need a catchy, professional flyer that will attract a very upscale clientele. Most of our students will be under the age of 5, but we want to attract older students as well. The project is to design a flyer that tells people about our school, and directs them to the website to enroll/get more information

Target Market(s)

Upscale, affluent parents who need care for and want to educate their children starting at a young age.

Industry/Entity Type

Education/Day Care

Font styles to use
Serif

Colors
59FF00
82FF00
B8FF75
E3FFCB
F4FFEA
6B429C
8869AF
B7A5CE
E3DAEB
F3F0F8

Requirements
Must have
• photos of children, a clean look
Nice to have
• Please see attached logo samples. I am going to use either 2a or 4a; those are the colors i would like to use
Should not have
• A cluttered look or too much information

```html
<!DOCTYPE html>
<html lang="en">
<head>
<meta charset="utf-8">
<title>Quiet Harbor Academy — Enroll Today</title>
<link href="https://fonts.googleapis.com/css2?family=Cormorant+Garamond:ital,wght@0,400;0,500;0,600;0,700;1,500&display=swap" rel="stylesheet">
<style>
  :root {
    --purple-deep: #6b429c;
    --purple-mid: #8869af;
    --purple-soft: #b7a5ce;
    --leaf: #bdd86f;
    --mist: #e6e9e0;
    --ink: #1c1a22;
    --white: #ffffff;
  }
  html, body { margin: 0; padding: 0; overflow: hidden; background: #f4f4f4; }
  .flyer {
    position: relative;
    width: 857px;
    height: 1200px;
    overflow: hidden;
    font-family: "Cormorant Garamond", Georgia, serif;
    background: var(--mist);
  }
  .backdrop { position: absolute; inset: 0; }
  .brand {
    position: absolute;
    top: 66px;
    left: 590px;
    width: 240px;
    text-align: center;
    color: var(--white);
    font-weight: 700;
    font-size: 30px;
    line-height: 28px;
    letter-spacing: -0.5px;
  }
  .quote {
    position: absolute;
    top: 414px;
    left: 250px;
    width: 600px;
    text-align: center;
    font-style: italic;
    font-weight: 500;
    font-size: 27px;
    line-height: 36px;
    color: var(--ink);
    margin: 0;
  }
  .quote cite { display: block; font-style: italic; margin-left: 90px; }
  .headline { position: absolute; left: 0; top: 0; }
  .feature {
    position: absolute;
    left: 310px;
    width: 545px;
    color: var(--white);
  }
  .feature h2 {
    margin: 0;
    font-weight: 500;
    font-size: 27px;
    line-height: 30px;
    letter-spacing: 0.3px;
  }
  .feature p {
    margin: 0;
    font-weight: 500;
    font-size: 17.5px;
    line-height: 24px;
    letter-spacing: 0.1px;
  }
  .feature--program { top: 660px; }
  .feature--family { top: 840px; }
  .feature--family p { line-height: 22px; }
  .feature--team { top: 1030px; }
  .feature--team p { line-height: 23.5px; }
  .contact {
    position: absolute;
    writing-mode: vertical-rl;
    color: var(--purple-deep);
    font-weight: 500;
    font-size: 23px;
    letter-spacing: 0.5px;
    line-height: 1;
    white-space: nowrap;
  }
  .contact--label { left: 70px; top: 636px; }
  .contact--web { left: 28px; top: 686px; }
  .contact--phone { left: 28px; top: 1034px; }
</style>
</head>
<body>
<div class="flyer">
  <svg class="backdrop" width="857" height="1200" viewBox="0 0 857 1200" xmlns="http://www.w3.org/2000/svg">
    <defs>
      <linearGradient id="photoTone" x1="0" y1="0" x2="1" y2="1">
        <stop offset="0" stop-color="#d9c39a"/>
        <stop offset="0.35" stop-color="#c98a66"/>
        <stop offset="0.65" stop-color="#d7c8c8"/>
        <stop offset="1" stop-color="#b9a9c4"/>
      </linearGradient>
      <linearGradient id="veil" x1="0" y1="0" x2="0" y2="1" gradientUnits="userSpaceOnUse">
        <stop offset="0.25" stop-color="#f1f2ec" stop-opacity="0.5"/>
        <stop offset="0.5" stop-color="#e6e9e0" stop-opacity="0.85"/>
        <stop offset="0.6" stop-color="#e6e9e0" stop-opacity="1"/>
      </linearGradient>
    </defs>

    <rect class="photo" x="0" y="0" width="857" height="700" fill="url(#photoTone)" role="img" aria-label="Photo of a smiling young girl in a gingham dress sitting in a bright classroom with other children behind her"/>

    <polygon class="veil-panel" points="37,478 857,232 857,1019 449,1019" fill="url(#veil)"/>
    <polygon class="leaf-panel" points="0,428 449,1019 857,1019 857,1200 0,1200" fill="var(--leaf)"/>

    <!-- feature bands -->
    <rect x="228" y="649" width="629" height="119" fill="var(--purple-deep)"/>
    <circle cx="230" cy="706" r="86" fill="var(--purple-deep)"/>
    <rect x="228" y="834" width="629" height="119" fill="var(--purple-mid)"/>
    <circle cx="230" cy="892" r="86" fill="var(--purple-mid)"/>
    <rect x="228" y="1019" width="629" height="118" fill="var(--purple-soft)"/>
    <circle cx="230" cy="1077" r="86" fill="var(--purple-soft)"/>

    <!-- growth chart icon -->
    <g class="icon-chart" fill="none" stroke="var(--white)" stroke-width="5" stroke-linecap="round" stroke-linejoin="round">
      <polyline points="185,664 185,751 280,751"/>
      <polyline points="177,672 185,659 193,672"/>
      <polyline points="271,743 280,751 271,759"/>
      <polyline points="203,720 226,703 247,716 269,690"/>
      <g fill="var(--white)" stroke="none">
        <circle cx="203" cy="720" r="8"/>
        <circle cx="226" cy="703" r="8"/>
        <circle cx="247" cy="716" r="8"/>
        <circle cx="269" cy="690" r="8"/>
      </g>
    </g>

    <!-- puzzle icon -->
    <g class="icon-puzzle" fill="var(--white)">
      <rect x="181" y="846" width="43" height="43" rx="3"/>
      <rect x="228" y="846" width="43" height="43" rx="3"/>
      <rect x="181" y="893" width="43" height="43" rx="3"/>
      <rect x="228" y="893" width="43" height="43" rx="3"/>
      <circle cx="226" cy="868" r="7"/>
      <circle cx="202" cy="891" r="7"/>
      <circle cx="250" cy="891" r="7" fill="var(--purple-mid)"/>
      <circle cx="226" cy="915" r="7" fill="var(--purple-mid)"/>
    </g>

    <!-- badge icon -->
    <g class="icon-badge">
      <circle cx="229" cy="1077" r="69" fill="var(--white)"/>
      <circle cx="229" cy="1077" r="53" fill="var(--purple-soft)"/>
      <polygon points="229,1058 235,1071 249,1072 238,1081 242,1095 229,1087 216,1095 220,1081 209,1072 223,1071" fill="var(--white)" stroke="var(--white)" stroke-width="4" stroke-linejoin="round"/>
    </g>

    <!-- contact markers -->
    <g class="marker-web">
      <circle cx="40" cy="657" r="22" fill="var(--purple-deep)"/>
      <circle cx="40" cy="657" r="12" fill="none" stroke="var(--white)" stroke-width="2.5"/>
      <path d="M30,652 Q40,660 50,652 M31,664 Q40,656 49,664 M40,645 Q34,657 40,669" fill="none" stroke="var(--white)" stroke-width="2"/>
    </g>
    <g class="marker-phone">
      <circle cx="43" cy="1005" r="22" fill="var(--purple-deep)"/>
      <path d="M48,996 q4,2 3,5 l-3,2 q-5,-1 -8,4 q-2,5 1,8 l-2,3 q-3,1 -5,-2 q-4,-8 3,-16 q6,-6 11,-4z" fill="var(--white)"/>
    </g>

    <text class="headline" x="124" y="598" textLength="710" lengthAdjust="spacingAndGlyphs"
      font-family="Cormorant Garamond, Georgia, serif" font-weight="600" font-size="92"
      fill="var(--purple-deep)">ENROLL TODAY</text>
  </svg>

  <div class="brand">Quiet Harbor<br>Academy</div>

  <blockquote class="quote">
    The education of a very small child does not aim at<br>
    preparing him for school but for life.
    <cite>-Dr. Elena Marchetti</cite>
  </blockquote>

  <section class="feature feature--program">
    <h2>Customized Educational Program</h2>
    <p>Start the joy of learning early with our Montessori Curriculum, providing opportunities for problem solving, lanuage development based on Research and Neurologically founded.</p>
  </section>

  <section class="feature feature--family">
    <h2>Family Support</h2>
    <p>We provide a welcoming atmosphere for parents and partners, working with you to answer questions, create community and redifine expectations for education to help students schieve their potential.</p>
  </section>

  <section class="feature feature--team">
    <h2>Top Notch Team</h2>
    <p>Our staffing team are talented and best in class professional teachers, Experienced school leader with 25+ years experience in beat schools in the country.</p>
  </section>

  <div class="contact contact--label">FOR MORE INFORMATION VISIT:</div>
  <div class="contact contact--web">WWW.WEBSITE.COM</div>
  <div class="contact contact--phone">NUMBER</div>
</div>
</body>
</html>
```